Business Cards

I'd like help creating business cards with the full logo "Veltrona Capital Partners" on the back of the card (navy background with white writing), and abbreviated logo "VCP" on the front. Would like to list name, title, phone number, email, and website listed on front of card. Would like to keep very simple. Front font Arial or similar.

```html
<!DOCTYPE html>
<html lang="en">
<head>
<meta charset="utf-8">
<title>Veltrona Capital Partners – Business Cards</title>
<link href="https://fonts.googleapis.com/css2?family=Poppins:wght@400;600;700&display=swap" rel="stylesheet">
<style>
  :root {
    --navy: #1d386b;
    --white: #ffffff;
    --ink-grey: #3b3f47;
    --backdrop-light: #d6d6d6;
    --backdrop-dark: #a9a9a9;
  }
  * { margin: 0; padding: 0; box-sizing: border-box; }
  html, body {
    width: 1200px;
    height: 800px;
    overflow: hidden;
  }
  body {
    background: linear-gradient(135deg, var(--backdrop-dark), var(--backdrop-light));
    font-family: "Poppins", Arial, sans-serif;
    position: relative;
  }
  .card {
    position: absolute;
    width: 560px;
    height: 320px;
    border-radius: 22px;
    overflow: hidden;
    box-shadow: 0 18px 40px rgba(0,0,0,0.28);
  }

  /* Front */
  .card-front {
    left: 50px;
    top: 70px;
    background: var(--white);
  }
  .front-corner-block {
    position: absolute;
    right: 0;
    top: 36px;
    width: 78px;
    height: 92px;
    background: var(--navy);
  }
  .holder {
    position: absolute;
    left: 44px;
    top: 96px;
  }
  .holder-name {
    color: var(--navy);
    font-weight: 700;
    font-size: 21px;
    letter-spacing: 0.5px;
    line-height: 1.1;
  }
  .holder-title {
    color: var(--ink-grey);
    font-weight: 400;
    font-size: 16px;
    line-height: 1.2;
  }
  .contact-band {
    position: absolute;
    left: 0;
    top: 178px;
    width: 320px;
    height: 96px;
    background: var(--navy);
    padding: 12px 0 0 44px;
  }
  .contact-row {
    display: flex;
    align-items: center;
    gap: 9px;
    color: var(--white);
    font-size: 15px;
    line-height: 24px;
  }
  .contact-row svg { width: 14px; height: 14px; flex: none; }
  .front-mark {
    position: absolute;
    left: 344px;
    top: 150px;
    display: flex;
    align-items: center;
    gap: 10px;
    color: var(--navy);
    font-weight: 700;
    font-size: 52px;
    letter-spacing: 1px;
    line-height: 1;
  }
  .front-mark .mark-square {
    width: 15px;
    height: 15px;
    background: var(--navy);
  }

  /* Back */
  .card-back {
    left: 590px;
    top: 400px;
    background: var(--navy);
    display: flex;
    flex-direction: column;
    align-items: center;
    justify-content: center;
    color: var(--white);
  }
  .back-mark {
    display: flex;
    align-items: center;
    gap: 12px;
  }
  .back-mark .mark-square {
    width: 18px;
    height: 18px;
    background: var(--white);
  }
  .company-name {
    font-weight: 700;
    font-size: 50px;
    letter-spacing: 2px;
    line-height: 1;
  }
  .company-tagline {
    margin-top: 12px;
    font-weight: 700;
    font-size: 17px;
    letter-spacing: 9px;
  }
</style>
</head>
<body>

  <section class="card card-front" aria-label="Business card front">
    <div class="front-corner-block"></div>

    <div class="holder">
      <p class="holder-name">MARCUS ELLERY</p>
      <p class="holder-title">Managing Director</p>
    </div>

    <div class="contact-band">
      <p class="contact-row">
        <svg viewBox="0 0 16 16" aria-hidden="true"><path fill="#fff" d="M3.6 1.2l2.3 2.6-1.3 1.6c.9 2 2.4 3.5 4.3 4.4l1.6-1.3 2.6 2.3-1.4 2.4C6.7 13.2 2.8 9.3 1.2 4.6z"/></svg>
        044-555 218 630
      </p>
      <p class="contact-row">
        <svg viewBox="0 0 16 16" aria-hidden="true"><rect x="1" y="3" width="14" height="10" fill="#fff"/><path d="M1 3l7 6 7-6" fill="none" stroke="#1d386b" stroke-width="1.4"/></svg>
        info@veltronacp.com
      </p>
      <p class="contact-row">
        <svg viewBox="0 0 16 16" aria-hidden="true"><g fill="none" stroke="#fff" stroke-width="1.3"><circle cx="8" cy="8" r="6.5"/><ellipse cx="8" cy="8" rx="3" ry="6.5"/><path d="M1.5 8h13M2.6 4.6h10.8M2.6 11.4h10.8"/></g></svg>
        www.veltronacp.com
      </p>
    </div>

    <div class="front-mark">
      <span class="mark-square"></span>
      <span>VCP</span>
    </div>
  </section>

  <section class="card card-back" aria-label="Business card back">
    <div class="back-mark">
      <span class="mark-square"></span>
      <span class="company-name">VELTRONA</span>
    </div>
    <p class="company-tagline">CAPITAL PARTNERS</p>
  </section>

</body>
</html>
```